Imported Fine Wine E-commerce site

We need an e-commerce site built from scratch. We currently have a website however it is on Magento and would like a more user friendly platform. Not sure if its possible to use any of the information. We're looking for a mostly white clean design with some red to match the logo.

Target Market(s)

30+

Coding

Coded - Design and coding required

Number of Pages Required

5+ page

Colors
ec1f27

Requirements
Must have
• Categories 'Red/White/Bubbles/Mixed cases/Gifts/Wholesale'
'sort by' functions.
Contact us form
Filter by on left hand side, Variety, Price, Region
Mobile friendly
Must be on a platform that i can update and make changes to it myself

```html
<!DOCTYPE html>
<html lang="en">
<head>
<meta charset="utf-8">
<title>Cepa Sur — Fine South American Wines</title>
<link rel="stylesheet" href="https://fonts.googleapis.com/css2?family=Playfair+Display:wght@600&family=Libre+Baskerville:wght@400&display=swap">
<style>
  :root {
    --red: #a51a2c;
    --ink: #1c1a1a;
    --white: #ffffff;
    --line: #e4e4e4;
    --wash: #eceff4;
    --bottle: #2a0f14;
    --sketch: #c9485c;
    --vine: #3f5a24;
    --soil: #2d2a1c;
  }
  * { box-sizing: border-box; margin: 0; padding: 0; }
  html, body { width: 1200px; height: 858px; overflow: hidden; background: var(--white); }
  .home { display: flex; width: 1200px; height: 858px; }
  .panel { position: relative; width: 600px; height: 858px; }
  .panel--shop { background: var(--white); }
  .panel--about {
    background: linear-gradient(180deg, #8fbccb 0%, #c9dbd8 24%, #8fb35f 36%, #6f9a42 46%, #4f7a2c 62%, var(--vine) 80%, var(--soil) 100%);
  }
  .brand {
    position: absolute;
    left: 32px;
    top: 40px;
    display: flex;
    align-items: center;
    gap: 8px;
    font-family: "Libre Baskerville", serif;
    font-size: 18px;
    color: var(--ink);
  }
  .brand-dot { width: 10px; height: 10px; border-radius: 50%; background: var(--red); }

  .art { position: absolute; }
  .art--wash {
    left: 159px; top: 44px; width: 256px; height: 440px;
    border-radius: 30% 40% 45% 35%;
    background: linear-gradient(160deg, var(--wash) 0%, #f3f5f8 70%, rgba(255,255,255,0) 100%);
  }
  .art--bottle {
    left: 258px; top: 72px; width: 84px; height: 436px;
    border-radius: 28px 28px 8px 8px;
    background: linear-gradient(180deg, #7a1a26 0%, #7a1a26 20%, var(--bottle) 24%, #1a0b0e 100%);
    z-index: 2;
  }
  .art--grapes {
    left: 372px; top: 132px; width: 152px; height: 222px;
    border-radius: 40% 40% 50% 50%;
    background: linear-gradient(180deg, #f1d7dc 0%, #e6a6b1 60%, #f3dde1 100%);
  }
  .art--sketch {
    left: 118px; top: 300px; width: 76px; height: 210px;
    border-radius: 30px 30px 10px 10px;
    background: linear-gradient(180deg, #f3dde1 0%, #e2a0ab 100%);
    z-index: 2;
  }

  .card {
    position: absolute;
    top: 478px;
    left: 101px;
    width: 390px;
    height: 290px;
    text-align: center;
    padding-top: 52px;
    z-index: 1;
  }
  .card--shop { border: 1px solid var(--line); background: transparent; }
  .card--about { left: 109px; background: rgba(255,255,255,0.9); }
  .card-title {
    font-family: "Playfair Display", serif;
    font-weight: 600;
    font-size: 41px;
    line-height: 1;
    color: var(--ink);
    position: relative;
    z-index: 3;
  }
  .card-text {
    margin-top: 22px;
    font-family: "Libre Baskerville", serif;
    font-size: 9.5px;
    color: var(--red);
  }
  .btn {
    display: inline-block;
    margin-top: 30px;
    width: 161px;
    height: 55px;
    line-height: 55px;
    font-family: "Libre Baskerville", serif;
    font-size: 11px;
    text-decoration: none;
  }
  .btn--solid { background: var(--red); color: var(--white); }
  .btn--outline { border: 1px solid #cfcfcf; color: var(--ink); line-height: 53px; }
  .menu-toggle {
    position: absolute;
    right: 32px;
    top: 44px;
    width: 43px;
    height: 54px;
    border: 1px solid rgba(255,255,255,0.85);
    display: flex;
    align-items: center;
    justify-content: center;
  }
</style>
</head>
<body>
<main class="home">
  <section class="panel panel--shop">
    <div class="brand"><span class="brand-dot"></span>Cepa Sur</div>
    <div class="art art--wash" role="img" aria-label="Soft grey watercolour wash behind the featured wine"></div>
    <div class="art art--grapes" role="img" aria-label="Red sketched illustration of a grape bunch with vine leaves"></div>
    <div class="art art--sketch" role="img" aria-label="Red sketched illustration of a bottle, glasses and cheese"></div>
    <div class="art art--bottle" role="img" aria-label="Photograph of a bottle of red wine"></div>
    <div class="card card--shop">
      <h2 class="card-title">Our Shop</h2>
      <p class="card-text">We deliver the best of South American wines directly to your door</p>
      <a class="btn btn--solid" href="#">See More</a>
    </div>
  </section>
  <section class="panel panel--about" role="img" aria-label="Photograph of vineyard rows below green hills and a blue sky">
    <div class="menu-toggle" aria-label="Menu">
      <svg width="18" height="10" viewBox="0 0 18 10"><g stroke="#ffffff" stroke-width="1"><line x1="0" y1="0.5" x2="18" y2="0.5"/><line x1="0" y1="5" x2="18" y2="5"/><line x1="0" y1="9.5" x2="18" y2="9.5"/></g></svg>
    </div>
    <div class="card card--about">
      <h2 class="card-title">About Us</h2>
      <p class="card-text">Cepa Sur was created with a simple but powerful vision</p>
      <a class="btn btn--outline" href="#">See More</a>
    </div>
  </section>
</main>
</body>
</html>
```